Business Card Design

Professional solutions in (servers, security, networks, programming)

Industry/Entity Type

Business

Contact Information for Business Card

Tarek Hounayni
Internet services and network solutions
DPV - RTLK - RTLB
netcare@qo-lam.com / 05917406238
www.qo-lam.com

```html
<!DOCTYPE html>
<html lang="en">
<head>
<meta charset="UTF-8">
<title>Tarek Hounayni — Business Card</title>
<link href="https://fonts.googleapis.com/css2?family=Arimo:wght@400;700&display=swap" rel="stylesheet">
<style>
  :root {
    --page-bg: #e4e2df;
    --card-bg: #f4f4f3;
    --band: #1d1d1d;
    --name: #ffffff;
    --gold: #c9953f;
    --ink: #2a2a2a;
    --cert: #1f1f1f;
  }
  * { margin: 0; padding: 0; box-sizing: border-box; }
  html, body {
    width: 1200px;
    height: 900px;
    overflow: hidden;
    background: var(--page-bg);
  }
  body {
    display: flex;
    align-items: center;
    justify-content: center;
    font-family: "Arimo", Arial, sans-serif;
  }
  .business-card {
    position: relative;
    width: 1000px;
    height: 572px;
    background: var(--card-bg);
    box-shadow: 0 6px 24px rgba(0,0,0,0.12);
  }
  .name-band {
    position: absolute;
    left: 0;
    top: 110px;
    width: 640px;
    height: 158px;
    background: var(--band);
    padding: 30px 0 0 88px;
  }
  .name {
    color: var(--name);
    font-size: 58px;
    font-weight: 400;
    letter-spacing: 2px;
    line-height: 1;
    text-transform: uppercase;
    white-space: nowrap;
  }
  .tagline {
    margin-top: 14px;
    color: var(--gold);
    font-size: 21px;
    letter-spacing: 1px;
    white-space: nowrap;
  }
  .contact-list {
    position: absolute;
    left: 96px;
    top: 300px;
    list-style: none;
  }
  .contact-item {
    display: flex;
    align-items: center;
    gap: 14px;
    height: 34px;
    color: var(--ink);
    font-size: 25px;
    letter-spacing: 1px;
  }
  .contact-icon {
    width: 24px;
    height: 24px;
    flex: none;
  }
  .certifications {
    position: absolute;
    left: 96px;
    top: 452px;
    color: var(--cert);
    font-size: 44px;
    font-weight: 700;
    letter-spacing: 1px;
    white-space: nowrap;
  }
</style>
</head>
<body>
  <article class="business-card">
    <header class="name-band">
      <h1 class="name">Tarek Hounayni</h1>
      <p class="tagline">Internet Services And Network Solutions</p>
    </header>

    <ul class="contact-list">
      <li class="contact-item">
        <svg class="contact-icon" viewBox="0 0 24 24" aria-hidden="true">
          <rect x="0" y="0" width="24" height="24" rx="5" fill="var(--band)"/>
          <rect x="8" y="4" width="8" height="16" rx="1.5" fill="none" stroke="var(--gold)" stroke-width="1.8"/>
          <circle cx="12" cy="17" r="1" fill="var(--gold)"/>
        </svg>
        <span class="contact-text">05917406238</span>
      </li>
      <li class="contact-item">
        <svg class="contact-icon" viewBox="0 0 24 24" aria-hidden="true">
          <rect x="0" y="0" width="24" height="24" rx="5" fill="var(--band)"/>
          <rect x="5" y="7" width="14" height="10" rx="1" fill="none" stroke="var(--gold)" stroke-width="1.8"/>
          <path d="M5 8 L12 13 L19 8" fill="none" stroke="var(--gold)" stroke-width="1.8"/>
        </svg>
        <span class="contact-text">netcare@qo-lam.com</span>
      </li>
      <li class="contact-item">
        <svg class="contact-icon" viewBox="0 0 24 24" aria-hidden="true">
          <rect x="0" y="0" width="24" height="24" rx="5" fill="var(--band)"/>
          <circle cx="12" cy="12" r="7" fill="none" stroke="var(--gold)" stroke-width="1.6"/>
          <ellipse cx="12" cy="12" rx="3" ry="7" fill="none" stroke="var(--gold)" stroke-width="1.3"/>
          <line x1="5" y1="12" x2="19" y2="12" stroke="var(--gold)" stroke-width="1.3"/>
        </svg>
        <span class="contact-text">www.qo-lam.com</span>
      </li>
    </ul>

    <p class="certifications">DPV - RTLK - RTLB</p>
  </article>
</body>
</html>
```